Design marketing/advertisement email for consulting business

Hello - My company, Brisbane-Orcutt, is looking for a marketing professional to compose a "marketing" email to be sent to potential professional referral sources. The email should provide an introduction of our company's capabilities and services. We want this marketing piece to invite the recipient to schedule a call with us to further discuss how we could best work together. The email must included elements of our brand. Our website is www.brisbaneorcutt-example.com and will provide you with all the details about our business as well as our logo, branding, contact details etc. Thanks so much!
Industry/Entity Type
Business

```html
<!DOCTYPE html>
<html lang="en">
<head>
<meta charset="utf-8">
<title>Brisbane-Orcutt – Smart Strategies for Senior Housing Investments</title>
<link href="https://fonts.googleapis.com/css2?family=Roboto:wght@400;700&family=Roboto+Condensed:wght@300;400;700&display=swap" rel="stylesheet">
<style>
  :root {
    --ink: #4a4a50;
    --charcoal: #404049;
    --coral: #dc735c;
    --peach: #f6b993;
    --peach-text: #f4ad85;
    --band: rgba(236,236,236,0.92);
    --white: #ffffff;
  }
  * { margin: 0; padding: 0; box-sizing: border-box; }
  html, body { width: 1000px; height: 1200px; overflow: hidden; background: #fff; }
  .flyer { position: relative; width: 1000px; height: 1200px; overflow: hidden; font-family: "Roboto Condensed", Arial, sans-serif; }

  .hero {
    position: absolute; left: 0; top: 0; width: 1000px; height: 610px;
    background:
      radial-gradient(ellipse 330px 260px at 500px 330px, #d9b08f 0%, #c9a383 35%, rgba(220,200,185,0.5) 65%, rgba(240,238,236,0) 100%),
      linear-gradient(180deg, #f6f6f6 0%, #ececec 60%, #e4e4e4 100%);
  }

  .brand { position: absolute; left: 50px; top: 50px; display: flex; align-items: center; gap: 12px; }
  .brand-square { width: 54px; height: 54px; background: var(--coral); }
  .brand-name { font-weight: 300; font-size: 34px; color: var(--ink); letter-spacing: 0.5px; text-transform: uppercase; }

  .contact { position: absolute; right: 50px; top: 44px; text-align: right; font-weight: 300; font-size: 23px; line-height: 29px; color: var(--ink); }
  .contact .call-invite { display: block; margin-top: 6px; font-weight: 400; font-size: 17px; line-height: 22px; color: var(--coral); }

  .headline {
    position: absolute; left: 0; top: 508px; width: 1000px; height: 98px;
    background: var(--band);
    text-align: center; font-family: "Roboto", Arial, sans-serif; font-weight: 700;
    font-size: 36px; line-height: 40px; color: #58585c; padding-top: 11px; letter-spacing: 0.5px;
  }

  .columns { position: absolute; left: 0; top: 605px; width: 1000px; height: 595px; display: flex; }
  .column { flex: 0 0 333px; display: flex; flex-direction: column; }
  .column:last-child { flex-basis: 334px; }
  .column-title {
    height: 60px; border-top: 6px solid; background: linear-gradient(180deg,#f1f1f1,#e6e6e6);
    text-align: center; font-family: "Roboto", Arial, sans-serif; font-weight: 700; font-size: 24px; line-height: 54px;
  }
  .column-body { flex: 1; color: var(--white); padding: 34px 0 0 24px; }
  .service { margin-bottom: 10px; }
  .service h3 { font-family: "Roboto", Arial, sans-serif; font-weight: 700; font-size: 16px; line-height: 20px; margin-bottom: 2px; }
  .service p { font-size: 12px; line-height: 15.3px; padding-left: 10px; }

  .development .column-title { border-color: var(--charcoal); color: var(--charcoal); }
  .development .column-body { background: var(--charcoal); padding-right: 26px; }
  .operation .column-title { border-color: var(--coral); color: var(--coral); }
  .operation .column-body { background: var(--coral); padding-left: 25px; padding-right: 28px; }
  .disposition .column-title { border-color: var(--peach); color: var(--peach-text); }
  .disposition .column-body { background: var(--peach); padding-left: 20px; padding-right: 22px; }
</style>
</head>
<body>
<div class="flyer">
  <div class="hero" role="img" aria-label="Open hands holding a model of a modern multi-storey senior housing building"></div>

  <div class="brand">
    <span class="brand-square"></span>
    <span class="brand-name">Brisbane-Orcutt</span>
  </div>

  <div class="contact">
    PHONE: 555.310.4826<br>
    FAX: 555.310.4830<br>
    info@brisbaneorcutt-example.com
    <span class="call-invite">Let's work together – schedule a call with us today.</span>
  </div>

  <h1 class="headline">SMART STRATEGIES FOR<br>SENIOR HOUSING INVESTMENTS</h1>

  <div class="columns">
    <section class="column development">
      <h2 class="column-title">DEVELOPMENT</h2>
      <div class="column-body">
        <div class="service">
          <h3>Feasibility Studies</h3>
          <p>Site selection studies, demographic reports and mystery shopping of the local competition are services offered to ensure that you are building your community in the best location possible to maximize your investment.</p>
        </div>
        <div class="service">
          <h3>Community Design and Pricing</h3>
          <p>Services offered include unit mix and community amenity recommendations, strategies for flexible unit types, pricing guidance for rents, programming, and care services and leasing strategies to achieve stabilized occupancy. These services will enable you to build a community that meets the demands of your chosen market and to achieve your financial objectives for your investment.</p>
        </div>
        <div class="service">
          <h3>Asset Management</h3>
          <p>Asset management services focus on assessing the reporting and budgeting needs of the investors, developers and management team at your community. Once these needs are assessed, customized reporting and budget templates are designed and provided to your operator for completion on a monthly, quarterly or annual basis. Establishing concise and accurate reports and budgets will allow you to easily assess your community's performance. These services are offered for both the construction/development phase and the operating phase.</p>
        </div>
      </div>
    </section>

    <section class="column operation">
      <h2 class="column-title">OPERATION</h2>
      <div class="column-body">
        <div class="service">
          <h3>Performance Audits</h3>
          <p>Detailed on-site audits of the community and operator are offered, along with resident and staff satisfaction surveys. Additional services include analysis of the community's occupancy trends, financial performance, tour conversion rates and discounting strategies to provide you with a complete picture of the community's performance. These services can be provided on a quarterly or annual basis.</p>
        </div>
        <div class="service">
          <h3>Market Updates</h3>
          <p>An assessment of the competitive landscape is offered with a focus on the competitions' current pricing strategies and occupancy. This service can be provided on a quarterly or annual basis and, when combined with a community performance audit, will enable you to make decisions about your community's pricing and position within the market.</p>
        </div>
        <div class="service">
          <h3>Asset Positioning</h3>
          <p>Asset positioning is offered for communities that are underperforming. Services include strategy reviews to determine the potential performance of the community and whether this asset should be a "hold" or "sell" for the investor, and repositioning options to rebalance the community's unit mix between IL, AL, and DEM and to expand programming to meet market demands.</p>
        </div>
      </div>
    </section>

    <section class="column disposition">
      <h2 class="column-title">DISPOSITION</h2>
      <div class="column-body">
        <div class="service">
          <h3>Asset Appraisals</h3>
          <p>Partnering with your selected external appraisal firm, this service ensures that your external appraiser bases their valuation on current and accurate community occupancy, performance and financial data and the most relevant market data and sales comps. Services include managing the distribution of information to the external appraisal firm and reviewing the initial and subsequent drafts of the valuation to ensure that the final valuation report is accurate. This service is offered on a quarterly, annual or one-time basis for investors preparing a community for sale.</p>
        </div>
        <div class="service">
          <h3>Operator Transitions</h3>
          <p>This service is geared for exiting investors who need to orchestrate the hand-over of their community to a new owner and/or operator. Transition services include ensuring that resident agreements are transferred in accordance with state regulations, integrating new pricing and programming, working with the outgoing operator to identify and retain key staff members, and communicating the transition to residents. The objective of these transitional services is to ensure a smooth handover to the new operator with minimized disturbances to the residents and to the community's operations.</p>
        </div>
        <div class="service">
          <h3>Community Communications</h3>
          <p>Services include orchestrating the communication plan to announce the sale of the community to residents and staff, and working with the new operator to ensure that daily operations and key staff are maintained until the closing of the sale.</p>
        </div>
      </div>
    </section>
  </div>
</div>
</body>
</html>
```